PTA Business Card

Seeking design for a business card, standard size. It is going to be for myself in regards to PTA - details:

Hollis Fernway Elementary School
PTA President
Neil Brawley
555-208-3147
Brawl1984@mailnest.example

Requirement:
Facebook icon? "Hollis Fernway PTA Durn"
Twitter thing? I am new to twitter so not sure what to put, here is the link:
https://twitter.com/HFRoverbirdsPTA

I was thinking on the front would be a notebook paper background? Not a requirement but was thinking it would look cool?

Total freedom here, let your creativity spread because I don't have any suggestions for design, sorry. Colors of school district are black and yellow.

Backside I am not sure exactly what to put on it.

```html
<!DOCTYPE html>
<html lang="en">
<head>
<meta charset="utf-8">
<title>Hollis Fernway PTA Business Card</title>
<link rel="stylesheet" href="https://fonts.googleapis.com/css2?family=Arvo:wght@400;700&family=Kalam:wght@400&family=Dancing+Script:wght@700&family=Tinos:wght@400&display=swap">
<style>
  :root {
    --backdrop: #d9d9d9;
    --paper: #ffffff;
    --rule: #c9d3e6;
    --margin-red: #ef8a93;
    --ink-black: #1a1a1a;
    --ink-blue: #2b3f9e;
    --wave-blue: #1f6fc0;
    --wave-yellow: #f6b51c;
    --marble-dark: #1c1c1c;
    --marble-light: #8a8a8a;
    --icon-teal: #2a9aa6;
    --lens-light: #eef1f5;
    --lens-edge: #a4abb4;
  }
  * { box-sizing: border-box; margin: 0; padding: 0; }
  html, body { width: 1200px; height: 754px; overflow: hidden; }
  body {
    background: var(--backdrop);
    display: flex;
    align-items: center;
    justify-content: center;
    gap: 60px;
  }
  .card {
    position: relative;
    width: 380px;
    height: 665px;
    overflow: hidden;
    box-shadow: 0 6px 18px rgba(0,0,0,.25);
  }

  /* Front: notebook paper */
  .card-front {
    background:
      linear-gradient(to right, transparent 30px, var(--margin-red) 30px, var(--margin-red) 32px, transparent 32px),
      repeating-linear-gradient(to bottom, var(--paper) 0, var(--paper) 25px, var(--rule) 25px, var(--rule) 27px);
    background-color: var(--paper);
  }
  .school-title {
    position: absolute;
    left: 44px; top: 14px;
    font-family: "Arvo", serif;
    font-weight: 700;
    color: var(--ink-black);
    line-height: 1;
  }
  .school-title .name { font-size: 34px; display: block; }
  .school-title .type { font-size: 19px; display: block; margin-top: 4px; }

  .handwritten { font-family: "Kalam", cursive; font-weight: 400; color: var(--ink-blue); position: absolute; left: 50px; white-space: nowrap; }
  .person-name { top: 110px; font-size: 32px; }
  .person-role { top: 152px; font-size: 17px; }

  .contact-row { display: flex; align-items: center; gap: 8px; }
  .contact-row .handwritten, .social-lines .handwritten { position: static; }
  .phone-row { position: absolute; left: 44px; top: 200px; }
  .phone-row .handwritten { font-size: 22px; }
  .email-row { position: absolute; left: 44px; top: 236px; }
  .email-row .handwritten { font-size: 14px; }

  .social-art {
    position: absolute;
    left: 22px; top: 292px;
    width: 86px; height: 86px;
    border-radius: 50%;
    background: radial-gradient(circle at 40% 40%, var(--lens-light) 0%, var(--lens-edge) 100%);
  }
  .social-lines { position: absolute; left: 112px; top: 300px; }
  .social-lines .handwritten { display: block; line-height: 1.5; }
  .social-lines .page-name { font-size: 16px; }
  .social-lines .handle { font-size: 20px; }

  .school-mark {
    position: absolute;
    right: 22px; top: 500px;
    display: flex;
    align-items: center;
    gap: 10px;
  }
  .mark-square {
    width: 28px; height: 28px;
    background: var(--wave-yellow);
  }
  .mark-text {
    font-family: "Arvo", serif;
    font-weight: 700;
    color: var(--ink-black);
    line-height: 1.1;
    text-align: center;
  }
  .mark-text .name { display: block; font-size: 21px; }
  .mark-text .type { display: block; font-size: 13px; }
  .front-wave { position: absolute; left: 0; bottom: 0; width: 380px; height: 110px; }

  /* Back: composition cover */
  .card-back { background: var(--marble-dark); }
  .cover-pattern {
    position: absolute; inset: 0;
    background: linear-gradient(160deg, var(--marble-light) 0%, #4d4d4d 45%, var(--marble-light) 100%);
  }
  .cover-label {
    position: absolute;
    left: 60px; top: 70px;
    width: 260px; height: 150px;
    background: var(--paper);
    border-radius: 12px;
    border: 2px solid #bdbdbd;
    text-align: center;
    padding-top: 14px;
  }
  .cover-label .label-name { font-family: "Arvo", serif; font-weight: 700; font-size: 24px; color: var(--ink-black); line-height: 1; }
  .cover-label .label-type { font-family: "Arvo", serif; font-weight: 700; font-size: 15px; color: var(--ink-black); margin-top: 3px; }
  .cover-label .label-person {
    font-family: "Dancing Script", cursive;
    font-weight: 700;
    font-size: 22px;
    color: var(--ink-black);
    border-bottom: 1px solid #777;
    margin: 6px 24px 0;
    line-height: 1.2;
  }
  .cover-label .label-role {
    font-family: "Tinos", serif;
    font-size: 15px;
    color: var(--ink-black);
    border-bottom: 1px solid #777;
    margin: 2px 24px 0;
  }
  .cover-label .label-line { border-bottom: 1px solid #777; margin: 14px 24px 0; }
</style>
</head>
<body>

<section class="card card-front" aria-label="Business card front">
  <h1 class="school-title">
    <span class="name">Hollis Fernway</span>
    <span class="type">Elementary School</span>
  </h1>

  <p class="handwritten person-name">Neil Brawley</p>
  <p class="handwritten person-role">PTA President</p>

  <div class="contact-row phone-row">
    <svg width="24" height="24" viewBox="0 0 24 24" aria-hidden="true">
      <rect x="1" y="1" width="22" height="22" rx="4" fill="var(--icon-teal)"/>
      <path d="M8 6c1 0 2 2.5 1.5 3.2l-1 1c.8 1.7 2.2 3.1 3.9 3.9l1-1c.7-.5 3.2.5 3.2 1.5 0 1.5-1.2 2.4-2.4 2.4C9.5 17 7 14.5 6 9.4 6 7.2 6.8 6 8 6z" fill="#fff"/>
    </svg>
    <span class="handwritten">555-208-3147</span>
  </div>

  <div class="contact-row email-row">
    <svg width="24" height="24" viewBox="0 0 24 24" aria-hidden="true">
      <circle cx="12" cy="12" r="11" fill="var(--icon-teal)"/>
    </svg>
    <span class="handwritten">Brawl1984@mailnest.example</span>
  </div>

  <div class="social-art" role="img" aria-label="Magnifying glass illustration over social media icons"></div>
  <div class="social-lines">
    <span class="handwritten page-name">Hollis Fernway PTA Durn</span>
    <span class="handwritten handle">@HFRoverbirdsPTA</span>
  </div>

  <div class="school-mark">
    <div class="mark-square" aria-hidden="true"></div>
    <div class="mark-text">
      <span class="name">Hollis Fernway</span>
      <span class="type">Elementary School</span>
    </div>
  </div>

  <svg class="front-wave" viewBox="0 0 380 110" preserveAspectRatio="none" aria-hidden="true">
    <path d="M0 70 C120 40 250 30 380 0 L380 30 C250 55 120 70 0 95 Z" fill="var(--wave-yellow)"/>
    <path d="M0 85 C120 60 250 45 380 25 L380 110 L0 110 Z" fill="var(--wave-blue)"/>
    <path d="M0 85 C120 60 250 45 380 25" fill="none" stroke="#fff" stroke-width="3"/>
  </svg>
</section>

<section class="card card-back" aria-label="Business card back">
  <div class="cover-pattern" role="img" aria-label="Black and white marbled composition notebook cover pattern"></div>
  <div class="cover-label">
    <div class="label-name">Hollis Fernway</div>
    <div class="label-type">Elementary School</div>
    <div class="label-person">Neil Brawley</div>
    <div class="label-role">PTA President</div>
    <div class="label-line"></div>
  </div>
</section>

</body>
</html>
```